New website

Our website (www.larchvale.com) needs to be replaced with something gorgeous and glossy. We do like the text of our current website but have many new images to put on the site. We want to create a website that shows viewers what our team can do, and how we can create something amazing for them and their homes.

Coding

```html
<!DOCTYPE html>
<html lang="en">
<head>
<meta charset="utf-8">
<title>Larchvale Landscaping</title>
<link rel="stylesheet" href="https://fonts.googleapis.com/css2?family=Ubuntu:wght@400;500;700&family=Open+Sans:wght@400;600;700&family=Cinzel:wght@400&display=swap">
<style>
:root{
  --green:#3fae5a;
  --green-light:#6cc47f;
  --navy:#131b35;
  --navy-text:#1c2847;
  --muted:#8a8f99;
  --pale:#eef2f6;
  --white:#fff;
  --teal:#3a86b0;
}
*{box-sizing:border-box;margin:0;padding:0}
html,body{width:1200px;height:4612px;overflow:hidden}
body{position:relative;font-family:"Open Sans",sans-serif;color:var(--navy-text);background:var(--white)}
.abs{position:absolute}
.label{font-family:"Open Sans",sans-serif;font-size:12px;font-weight:600;color:var(--green);text-decoration:underline;text-underline-offset:4px;letter-spacing:.3px}
.h2{font-family:"Ubuntu",sans-serif;font-weight:500;font-size:40px;color:var(--navy-text)}
.center{left:0;width:1200px;text-align:center}
.btn{display:flex;align-items:center;justify-content:center;gap:14px;background:var(--green);color:#fff;font-family:"Ubuntu",sans-serif;font-weight:500;font-size:16px;border-radius:2px}
.photo{position:absolute}

/* top bar */
.topbar{top:0;left:0;width:1200px;height:40px;font-size:12px;color:var(--muted);font-weight:600}
.topbar span{position:absolute;top:12px;display:flex;align-items:center;gap:6px}
.social{position:absolute;top:14px;width:10px;height:10px;border-radius:50%;background:#9aa3b5}

/* header */
.header{top:40px;left:0;width:1200px;height:122px;background:var(--navy)}
.brand{position:absolute;left:108px;top:32px;font-family:"Open Sans",sans-serif;font-size:28px;letter-spacing:6px;color:var(--green);font-weight:400}
.badge{position:absolute;top:30px;display:flex;gap:14px;align-items:center;color:#fff;font-size:12px;font-weight:700;line-height:1.3}
.nav{top:125px;left:91px;width:996px;height:68px;background:#fff;box-shadow:0 4px 14px rgba(0,0,0,.12)}
.nav a{position:absolute;top:24px;font-size:15px;color:var(--navy-text);text-decoration:none}
.nav .active{border-bottom:3px solid var(--green);padding-bottom:20px;padding-left:20px;padding-right:20px;left:32px!important}
.quote{position:absolute;right:28px;top:15px;width:152px;height:38px;border-radius:20px;background:var(--green-light);color:#fff;font-size:14px;font-weight:600;display:flex;align-items:center;justify-content:center}

/* hero */
.hero-title{left:235px;top:385px;width:728px;height:81px;background:rgba(63,174,90,.88);color:#fff;font-family:"Cinzel",serif;font-size:48px;display:flex;align-items:center;justify-content:center;letter-spacing:1px}
.hero-text{left:159px;top:469px;width:883px;height:83px;background:rgba(15,20,30,.88);color:#fff;font-size:19px;font-weight:600;text-align:center;padding-top:12px;line-height:1.4}

/* services cards */
.card{position:absolute;top:1805px;width:306px;height:210px;background:#fff;box-shadow:0 4px 16px rgba(0,0,0,.08);text-align:center}
.card .img{position:absolute;left:16px;top:-32px;width:274px;height:158px;border-radius:4px}
.card .ico{position:absolute;right:16px;top:76px;width:54px;height:54px;border-radius:50%;background:var(--green-light);display:flex;align-items:center;justify-content:center}
.card .small{position:absolute;top:142px;width:100%;font-size:11px;font-weight:700;color:var(--green)}
.card .name{position:absolute;top:162px;width:100%;font-family:"Ubuntu",sans-serif;font-size:19px;font-weight:500;color:var(--navy-text)}

/* why */
.why-ring{position:absolute;top:2434px;width:96px;height:96px;border-radius:50%;border:8px solid var(--green);background:#fff;display:flex;align-items:center;justify-content:center}
.why-box{position:absolute;top:2418px;width:215px;height:125px;border:2px dashed #fff;border-radius:6px;color:#fff;padding:14px 20px 0 24px}
.why-box h4{font-family:"Ubuntu",sans-serif;font-weight:500;font-size:17px;margin-bottom:6px}
.why-box p{font-size:11px;line-height:1.35}
.why-dot{position:absolute;top:2474px;width:16px;height:16px;border-radius:50%;background:var(--green);border:3px solid var(--navy)}

/* reviews */
.review{position:absolute;top:2937px;width:304px;height:166px;background:#fff;box-shadow:0 4px 16px rgba(0,0,0,.07)}
.review p{position:absolute;left:32px;top:40px;width:255px;font-size:14px;line-height:1.75;color:var(--muted)}
.review .q{position:absolute;right:22px;top:-8px;font-family:"Ubuntu",sans-serif;font-size:64px;font-weight:700;color:var(--green);line-height:1}
.avatar{position:absolute;top:2833px;width:90px;height:104px}
.person{position:absolute;top:2854px}
.person b{display:block;font-family:"Ubuntu",sans-serif;font-weight:500;font-size:18px}
.person small{font-size:12px;color:var(--muted)}

/* contact */
.info-row{position:absolute;left:150px;display:flex;gap:34px;align-items:center;font-size:14px;color:var(--muted)}
.form{left:591px;top:3421px;width:485px;height:520px;border-top:3px solid var(--teal);border-radius:12px 12px 0 0}
.field-label{position:absolute;font-size:14px;font-weight:700;color:var(--teal)}
.field{position:absolute;height:43px;border:1px solid #c9ced6;border-radius:2px;font-size:12px;color:var(--muted);padding:14px 16px}

/* footer */
.footer{top:4040px;left:0;width:1200px;height:572px;background:var(--navy);color:#fff}
.footer h3{position:absolute;font-family:"Ubuntu",sans-serif;font-weight:500;font-size:22px}
.footer .bar{position:absolute;width:44px;height:4px;background:var(--green);border-radius:2px}
.links{position:absolute;font-size:15px;line-height:30.5px}
.links div::before{content:"›";margin-right:14px;font-size:18px}
.infobar{position:absolute;left:84px;top:4472px;width:1027px;height:104px;background:#2c344b;border-radius:4px;color:#fff}
.info-cell{position:absolute;top:22px;display:flex;gap:22px;align-items:center;font-size:16px;line-height:1.5;color:#fff}
.info-cell b{font-size:15px}
.footnote{position:absolute;top:4584px;font-size:13px;color:var(--navy-text)}
</style>
</head>
<body>

<!-- Top bar -->
<div class="abs topbar">
  <span style="left:88px"><svg width="14" height="14" viewBox="0 0 24 24"><path d="M6 2l4 4-2 3c1 3 4 6 7 7l3-2 4 4-3 4C10 21 3 14 2 5z" fill="var(--green)"/></svg>(555) 214-0386</span>
  <span style="left:240px">|&nbsp;&nbsp;<svg width="14" height="12" viewBox="0 0 24 18"><rect width="24" height="18" rx="2" fill="var(--green)"/><path d="M1 2l11 8 11-8" stroke="#fff" stroke-width="2" fill="none"/></svg>info@larchvale.com&nbsp;|</span>
  <span style="left:424px"><svg width="12" height="14" viewBox="0 0 24 30"><path d="M12 0a10 10 0 0110 10c0 8-10 20-10 20S2 18 2 10A10 10 0 0112 0z" fill="var(--green)"/><circle cx="12" cy="10" r="4" fill="#fff"/></svg>48 Orchard Row</span>
  <i class="social" style="left:988px"></i><i class="social" style="left:1015px"></i><i class="social" style="left:1042px"></i><i class="social" style="left:1069px"></i>
</div>

<!-- Header -->
<div class="abs header">
  <div class="brand">LARCHVALE</div>
  <div class="badge" style="left:806px"><svg width="26" height="26" viewBox="0 0 26 26"><circle cx="13" cy="13" r="11" stroke="var(--green)" stroke-width="2" fill="none"/><path d="M13 7v6l-4 3" stroke="var(--green)" stroke-width="2" fill="none"/></svg><div>24/7<br>Service</div></div>
  <div class="abs" style="left:938px;top:22px;width:2px;height:42px;background:#fff"></div>
  <div class="badge" style="left:966px"><svg width="22" height="22" viewBox="0 0 24 24"><path d="M3 11h4v10H3zM7 11l5-8c2 0 3 1 2 4l-1 3h7c1 0 2 1 2 2l-2 7c0 1-1 2-2 2H7" stroke="var(--green)" stroke-width="2" fill="none"/></svg><div>Qualified<br>Professionals</div></div>
</div>

<!-- Hero -->
<div class="photo" role="img" aria-label="Gardener trimming grass with a string trimmer in a green park" style="left:0;top:161px;width:1200px;height:660px;background:radial-gradient(circle at 55% 35%,#8a8f6c 0,#5f7d3a 22%,#4f7a2e 45%,#76963f 70%,#a3b56c 100%)"></div>
<svg class="abs" style="left:0;top:640px" width="1200" height="240" viewBox="0 0 1200 240">
  <path d="M0 30 C300 210 800 230 1200 100 L1200 240 L0 240Z" fill="#fff"/>
  <path d="M0 30 C300 200 820 230 1200 96 C850 210 420 200 0 34Z" fill="var(--green)"/>
</svg>
<div class="abs nav">
  <a class="active" style="left:32px">Home</a>
  <a style="left:198px">About Us</a>
  <a style="left:335px">Services</a>
  <a style="left:482px">Our Team</a>
  <a style="left:622px">Contact Us</a>
  <div class="quote">Get A Quote</div>
</div>
<div class="abs hero-title">LANDSCAPING EXPERTS</div>
<div class="abs hero-text">Lorem ipsum dolor sit amet, consectetur adipiscing elit, sed do eiusmod tempor incididunt ut labore et dolore magna aliqua. Ut enim ad minim</div>

<!-- About -->
<svg class="abs" style="left:100px;top:920px" width="490" height="490" viewBox="0 0 490 490">
  <path d="M14 190 A232 232 0 1 1 250 476" stroke="var(--green)" stroke-width="8" fill="none"/>
</svg>
<div class="photo" role="img" aria-label="Gardener trimming a tall hedge with a hedge cutter" style="left:120px;top:944px;width:448px;height:448px;border-radius:50%;background:radial-gradient(circle at 60% 55%,#4f6a3a,#2f4a24 60%,#1f3419)"></div>
<div class="abs label" style="left:631px;top:955px">WHO WE ARE</div>
<div class="abs" style="left:630px;top:985px;font-family:Ubuntu,sans-serif;font-size:41px;font-weight:500;line-height:53px;color:var(--navy-text)">The team you can trust<br>to get the job done</div>
<div class="abs" style="left:630px;top:1118px;font-family:Ubuntu,sans-serif;font-size:22px">Outdoor Spaces, Reimagined</div>
<div class="abs" style="left:630px;top:1164px;width:505px;font-size:12.5px;line-height:22px;color:var(--muted)">Lorem ipsum dolor sit amet, consectetur adipiscing elit, sed do eiusmod tempor incididunt ut labore et dolore magna aliqua. Ut enim ad minim veniam, quis nos trud exercitation ullamco laboris nisi ut aliquip ex ea commodo consequat.<br>Duis aute irure dolor in reprehenderit in voluptate velit esse cillum dolore eu fugiat nulla pariatur. Excepteur sint occaecat cupidatat non proident, sunt in culpa qui officia deserunt mollit anim id est laborum.</div>
<div class="abs btn" style="left:629px;top:1325px;width:155px;height:44px">Contact us <span>→</span></div>

<!-- Services -->
<svg class="abs" style="left:0;top:1450px" width="1200" height="780" viewBox="0 0 1200 780">
  <path d="M0 90 C380 -60 850 40 1200 175 L1200 744 L0 744Z" fill="var(--pale)"/>
  <path d="M0 90 C380 -62 860 30 1200 168 C850 50 400 -30 0 100Z" fill="var(--green)"/>
</svg>
<div class="abs label center" style="top:1624px">OUR SERVICES</div>
<div class="abs h2 center" style="top:1660px">Services We Offer</div>
<div class="card" style="left:122px"><div class="img" role="img" aria-label="Workers laying turf rolls" style="background:linear-gradient(160deg,#4a6a3a,#3b4a2c 55%,#6a7a4a)"></div><div class="ico"><svg width="28" height="28" viewBox="0 0 24 24"><path d="M12 2l3 7h7l-5.5 4.5 2 7.5-6.5-4.5-6.5 4.5 2-7.5L2 9h7z" stroke="#fff" stroke-width="1.6" fill="none" stroke-linejoin="round"/></svg></div><div class="small">OUR SERVICES</div><div class="name">Landscape Design</div></div>
<div class="card" style="left:449px"><div class="img" role="img" aria-label="Gardener checking plants in a greenhouse" style="background:linear-gradient(160deg,#b7c7a8,#6f8f55 55%,#4f6e3a)"></div><div class="ico"><svg width="28" height="28" viewBox="0 0 24 24"><path d="M12 2l3 7h7l-5.5 4.5 2 7.5-6.5-4.5-6.5 4.5 2-7.5L2 9h7z" stroke="#fff" stroke-width="1.6" fill="none" stroke-linejoin="round"/></svg></div><div class="small">OUR SERVICES</div><div class="name">Irrigation Systems</div></div>
<div class="card" style="left:779px"><div class="img" role="img" aria-label="Workers with hard hats installing outdoor lighting" style="background:linear-gradient(160deg,#8a5a3a,#c46a2a 45%,#6f5a45)"></div><div class="ico"><svg width="28" height="28" viewBox="0 0 24 24"><path d="M12 2l3 7h7l-5.5 4.5 2 7.5-6.5-4.5-6.5 4.5 2-7.5L2 9h7z" stroke="#fff" stroke-width="1.6" fill="none" stroke-linejoin="round"/></svg></div><div class="small">OUR SERVICES</div><div class="name">Outdoor Lighting</div></div>
<div class="abs btn" style="left:520px;top:2085px;width:155px;height:44px">Contact us <span>→</span></div>

<!-- Why -->
<div class="abs" style="left:0;top:2194px;width:1200px;height:424px;background:linear-gradient(120deg,#131b35,#1a2548 60%,#131b35)"></div>
<div class="abs center" style="top:2270px;font-size:12px;font-weight:600;color:#fff;text-decoration:underline;text-underline-offset:4px">WHY CHOOSE US</div>
<div class="abs h2 center" style="top:2305px;color:#fff">Why we are the Best</div>
<div class="why-ring" style="left:63px"><svg width="38" height="38" viewBox="0 0 24 24"><path d="M12 2l3 7h7l-5.5 4.5 2 7.5-6.5-4.5-6.5 4.5 2-7.5L2 9h7z" stroke="var(--green)" stroke-width="1.4" fill="none" stroke-linejoin="round"/></svg></div><i class="why-dot" style="left:176px"></i>
<div class="why-box" style="left:184px"><h4>Professional</h4><p>Lorem ipsum dolor sit amet, consectetur adipiscing elit, sed do eiusmod tem Lorem ipsum dolor sdolor s</p></div>
<div class="why-ring" style="left:432px"><svg width="38" height="38" viewBox="0 0 24 24"><path d="M12 2l3 7h7l-5.5 4.5 2 7.5-6.5-4.5-6.5 4.5 2-7.5L2 9h7z" stroke="var(--green)" stroke-width="1.4" fill="none" stroke-linejoin="round"/></svg></div><i class="why-dot" style="left:544px"></i>
<div class="why-box" style="left:552px"><h4>Client centric</h4><p>Lorem ipsum dolor sit amet, consectetur adipiscing elit, sed do eiusmod tem Lorem ipsum dolor sdolor s</p></div>
<div class="why-ring" style="left:801px"><svg width="38" height="38" viewBox="0 0 24 24"><path d="M12 2l3 7h7l-5.5 4.5 2 7.5-6.5-4.5-6.5 4.5 2-7.5L2 9h7z" stroke="var(--green)" stroke-width="1.4" fill="none" stroke-linejoin="round"/></svg></div><i class="why-dot" style="left:913px"></i>
<div class="why-box" style="left:921px"><h4>Experienced</h4><p>Lorem ipsum dolor sit amet, consectetur adipiscing elit, sed do eiusmod tem Lorem ipsum dolor sdolor s</p></div>

<!-- Reviews -->
<svg class="abs" style="left:0;top:2618px" width="1200" height="700" viewBox="0 0 1200 700">
  <path d="M0 0 H1200 V610 C850 730 300 700 0 560Z" fill="var(--pale)"/>
  <path d="M0 560 C320 690 850 720 1200 610 C860 700 330 690 0 552Z" fill="var(--green)"/>
</svg>
<div class="abs label center" style="top:2698px">TESTIMONIALS</div>
<div class="abs h2 center" style="top:2733px">Clients Reviews</div>

<div class="review" style="left:111px"><span class="q">”</span><p>Lorem ipsum dolor sit amet, consect etur adipiscing elit, sed do eiusmod tempor incididunt ut labore et dolore magna aliqua. Ut enim ad minim veni am, quis nostrud</p></div>
<div class="avatar" role="img" aria-label="Client portrait" style="left:90px;background:linear-gradient(#e4e6ea,#b9bfc9)"></div>
<div class="person" style="left:204px"><b>Marcus Denholm</b><small>CEO &amp; Founder</small></div>

<div class="review" style="left:459px"><span class="q">”</span><p>Lorem ipsum dolor sit amet, consect etur adipiscing elit, sed do eiusmod tempor incididunt ut labore et dolore magna aliqua. Ut enim ad minim veni am, quis nostrud</p></div>
<div class="avatar" role="img" aria-label="Client portrait" style="left:438px;background:linear-gradient(#e4e6ea,#9aa1ad)"></div>
<div class="person" style="left:545px"><b>Marcus Denholm</b><small>CEO &amp; Founder</small></div>

<div class="review" style="left:805px"><span class="q">”</span><p>Lorem ipsum dolor sit amet, consect etur adipiscing elit, sed do eiusmod tempor incididunt ut labore et dolore magna aliqua. Ut enim ad minim veni am, quis nostrud</p></div>
<div class="avatar" role="img" aria-label="Client portrait" style="left:787px;background:linear-gradient(#e4e6ea,#3a3f4a)"></div>
<div class="person" style="left:886px"><b>Marcus Denholm</b><small>CEO &amp; Founder</small></div>

<div class="abs btn" style="left:520px;top:3178px;width:155px;height:44px">Contact us <span>→</span></div>

<!-- Contact -->
<div class="abs" style="left:141px;top:3480px;font-family:Ubuntu,sans-serif;font-size:33px;line-height:44px"><b style="font-weight:500">Get&nbsp; in Touch</b><br><span style="color:var(--teal);font-weight:400">Contact Us</span></div>
<div class="abs" style="left:141px;top:3580px;width:360px;font-size:13px;line-height:24px;color:var(--muted)">Lorem ipsum dolor sit amet, consectetur adipiscing e lit, sed do eiusmod tempor incididunt ut labore et dolore magna aliqua. ceptos ...</div>
<div class="abs" style="left:141px;top:3686px;width:380px;height:1px;background:#d7dbe1"></div>
<div class="info-row" style="top:3726px"><svg width="14" height="18" viewBox="0 0 24 30"><path d="M12 0a10 10 0 0110 10c0 8-10 20-10 20S2 18 2 10A10 10 0 0112 0z" fill="var(--teal)"/><circle cx="12" cy="10" r="4" fill="#fff"/></svg>Fernhill Lane 12, 3390 Brookdale</div>
<div class="info-row" style="top:3788px"><svg width="14" height="14" viewBox="0 0 24 24"><path d="M6 2l4 4-2 3c1 3 4 6 7 7l3-2 4 4-3 4C10 21 3 14 2 5z" fill="var(--teal)"/></svg>+1 555 0142 778</div>
<div class="info-row" style="top:3843px"><svg width="14" height="12" viewBox="0 0 24 18"><rect width="24" height="18" rx="2" fill="var(--teal)"/><path d="M1 2l11 8 11-8" stroke="#fff" stroke-width="2" fill="none"/></svg>office@larchvale.com</div>

<div class="abs form"></div>
<div class="field-label" style="left:625px;top:3466px">Full Name:</div>
<div class="field" style="left:620px;top:3500px;width:425px">Sed non neque elit.</div>
<div class="field-label" style="left:625px;top:3570px">Email :</div>
<div class="field-label" style="left:851px;top:3570px">Phone no :</div>
<div class="field" style="left:620px;top:3603px;width:198px">Sed non neque elit.</div>
<div class="field" style="left:847px;top:3603px;width:198px">Sed non neque elit.</div>
<div class="field-label" style="left:625px;top:3682px">Messages &nbsp;:</div>
<div class="field" style="left:620px;top:3715px;width:425px;height:130px">Sed non neque elit.</div>
<div class="abs" style="left:620px;top:3871px;width:127px;height:41px;background:var(--green);color:#fff;font-weight:700;font-size:14px;display:flex;align-items:center;justify-content:center">SUBMIT</div>

<!-- Footer -->
<div class="abs footer">
  <div class="brand" style="left:84px;top:94px">LARCHVALE</div>
  <div class="abs" style="left:84px;top:152px;font-size:19px;font-weight:700">555-019-2244</div>
  <div class="abs" style="left:86px;top:184px;font-size:14px;font-weight:700">Call for free consultation</div>
  <div class="abs" style="left:86px;top:222px;width:290px;font-size:13px;line-height:22px">Lorem ipsum dolor sit amet, consectet sed do eiusmod tempor incididunt ut la magna aliqua. Ut enim</div>
  <div class="abs" style="left:86px;top:307px;font-size:14px;font-weight:700">Read more &nbsp;›</div>

  <h3 style="left:438px;top:86px">Useful Links</h3><i class="bar" style="left:438px;top:126px"></i>
  <div class="links" style="left:440px;top:150px"><div>About Company</div><div>Leadership</div><div>Blog Post</div><div>FAQ'S</div><div>Certification</div><div>Testimonials</div></div>
  <div class="links" style="left:606px;top:150px"><div>Services</div><div>Industries</div><div>Feedback</div><div>Partners</div><div>Pricing</div><div>Contct</div></div>

  <h3 style="left:789px;top:86px">Newsletter</h3><i class="bar" style="left:789px;top:126px"></i>
  <div class="abs" style="left:786px;top:186px;width:330px;font-size:12px;font-weight:600;line-height:22px">Dont miss to subscribe to our news feeds. kindly fill the form below</div>
  <div class="abs" style="left:788px;top:258px;width:266px;height:46px;background:#1b2440;border-radius:23px 0 0 23px;font-size:13px;font-weight:600;padding:14px 24px">Your Email Address</div>
  <div class="abs" style="left:1054px;top:258px;width:52px;height:46px;background:var(--green);border-radius:0 23px 23px 0;display:flex;align-items:center;justify-content:center;font-size:26px">›</div>
</div>
<div class="infobar">
  <div class="info-cell" style="left:30px"><svg width="28" height="34" viewBox="0 0 24 30"><path d="M12 1a10 10 0 0110 10c0 8-10 18-10 18S2 19 2 11A10 10 0 0112 1z" stroke="var(--green)" stroke-width="2" fill="none"/><circle cx="12" cy="11" r="4" stroke="var(--green)" stroke-width="2" fill="none"/></svg><div><b>Location</b><br>18 Hollow Rd, Ashford 02114</div></div>
  <div class="abs" style="left:342px;top:18px;width:1px;height:68px;background:#4a5268"></div>
  <div class="info-cell" style="left:372px"><svg width="30" height="28" viewBox="0 0 30 28"><path d="M2 2h26v18H10l-6 6v-6H2z" stroke="var(--green)" stroke-width="2" fill="none"/><path d="M8 9h14M8 14h10" stroke="var(--green)" stroke-width="2"/></svg><div><b>Mail us</b><br>support@larchvale.com</div></div>
  <div class="abs" style="left:686px;top:18px;width:1px;height:68px;background:#4a5268"></div>
  <div class="info-cell" style="left:714px"><svg width="30" height="30" viewBox="0 0 30 30"><path d="M28 2L2 12l10 4 4 10z M12 16L28 2" stroke="var(--green)" stroke-width="2" fill="none"/></svg><div><b>Office hrs</b><br>9.00am to 7.00pm (Mon-Sat)</div></div>
</div>
<div class="abs" style="left:0;top:4576px;width:1200px;height:36px;background:#fff"></div>
<div class="footnote" style="left:86px">Larchvale</div>
<div class="footnote" style="left:800px;word-spacing:2px">Privacy Policy &nbsp;&nbsp;&nbsp; Terms &amp; Conditions &nbsp;&nbsp;&nbsp; Site Map</div>
<div class="abs" style="left:1124px;top:4538px;width:50px;height:48px;background:var(--green);border-radius:3px;display:flex;align-items:center;justify-content:center"><svg width="20" height="14" viewBox="0 0 20 14"><path d="M2 12l8-8 8 8" stroke="#fff" stroke-width="3" fill="none"/></svg></div>

</body>
</html>
```